Bref créative
Business Card for Education Consulting Company
Brio Study Mentors
Simple
Marcus Delavine
President
317 Hollins Court NE
Washington DC 20019
Marcus@briostudymentors-example.com
www.briostudymentors-example.com
Looking for a simple, clean and professional business card. The logo already has the name of the company so there is no need to include again unless you feel it adds to the overall look of the card.
Here is the compnay's logo

```html
<!DOCTYPE html>
<html lang="en">
<head>
<meta charset="utf-8">
<title>Brio Study Mentors – Business Card</title>
<link rel="stylesheet" href="https://fonts.googleapis.com/css2?family=Cormorant+Garamond:wght@400;500;600&display=swap">
<style>
  :root {
    --page: #ece9e4;
    --card: #ffffff;
    --brand-blue: #1f55b4;
    --ink: #4a4a4a;
    --band-grey: #6f7072;
  }
  * { margin: 0; padding: 0; box-sizing: border-box; }
  html, body {
    width: 1200px; height: 914px; overflow: hidden;
    background: var(--page);
  }
  .canvas { position: relative; width: 1200px; height: 914px; }
  .card {
    position: absolute; left: 75px; top: 157px;
    width: 1050px; height: 600px;
    background: var(--card);
    box-shadow: 0 10px 30px rgba(0,0,0,0.15);
    overflow: hidden;
    font-family: "Cormorant Garamond", Georgia, serif;
  }
  .card-bands { position: absolute; left: 0; top: 0; }
  .brand {
    position: absolute; left: 0; right: 0; top: 95px;
    display: flex; align-items: center; justify-content: center; gap: 18px;
  }
  .brand-mark {
    width: 46px; height: 46px; border-radius: 50%;
    background: var(--brand-blue);
  }
  .brand-name {
    font-weight: 600; font-size: 50px; letter-spacing: 2px;
    color: var(--brand-blue); text-transform: uppercase;
  }
  .holder {
    position: absolute; left: 420px; top: 220px;
    text-align: center; width: 300px;
  }
  .holder-name {
    font-variant: small-caps; font-weight: 500; font-size: 32px;
    color: var(--brand-blue); letter-spacing: 1px;
  }
  .holder-title {
    font-variant: small-caps; font-size: 22px; color: var(--ink);
    letter-spacing: 1px; margin-top: -2px;
  }
  .address {
    position: absolute; right: 550px; top: 306px;
    text-align: right; font-variant: small-caps; font-size: 23px;
    color: var(--ink); line-height: 30px; letter-spacing: 1px;
  }
  .contacts {
    position: absolute; left: 512px; top: 302px;
    list-style: none; font-size: 19px; color: var(--ink);
    line-height: 30px; letter-spacing: 0.5px;
  }
  .contacts li { display: flex; align-items: center; gap: 10px; }
  .contacts svg { flex: none; }
</style>
</head>
<body>
<div class="canvas">
  <div class="card">
    <svg class="card-bands" width="1050" height="600" viewBox="0 0 1050 600" aria-hidden="true">
      <polygon points="0,420 470,420 500,450 0,450" fill="var(--brand-blue)"/>
      <polygon points="480,420 1050,420 1050,475 535,475" fill="var(--band-grey)"/>
    </svg>

    <div class="brand">
      <span class="brand-mark"></span>
      <span class="brand-name">Brio Study Mentors</span>
    </div>

    <div class="holder">
      <div class="holder-name">Marcus Delavine</div>
      <div class="holder-title">President</div>
    </div>

    <div class="address">
      317 Hollins Court NE<br>
      Washington DC 20019
    </div>

    <ul class="contacts">
      <li>
        <svg width="18" height="18" viewBox="0 0 18 18"><circle cx="9" cy="9" r="9" fill="var(--brand-blue)"/><path d="M6 5l2 2-1 1c.6 1.3 1.7 2.4 3 3l1-1 2 2-1.5 1.5C8 13 5 10 4.5 6.5z" fill="#fff"/></svg>
        703-555-0148
      </li>
      <li>
        <svg width="18" height="18" viewBox="0 0 18 18"><circle cx="9" cy="9" r="9" fill="var(--brand-blue)"/><rect x="4.5" y="6" width="9" height="6.5" fill="#fff"/><path d="M4.5 6l4.5 3.5L13.5 6" stroke="var(--brand-blue)" stroke-width="1" fill="none"/></svg>
        Marcus@briostudymentors-example.com
      </li>
      <li>
        <svg width="18" height="18" viewBox="0 0 18 18"><circle cx="9" cy="9" r="9" fill="var(--brand-blue)"/><circle cx="9" cy="9" r="4.5" stroke="#fff" stroke-width="1.2" fill="none"/><path d="M4.5 9h9M9 4.5v9" stroke="#fff" stroke-width="1"/></svg>
        www.briostudymentors-example.com
      </li>
    </ul>
  </div>
</div>
</body>
</html>
```